" Inteligência Artificial (IA), Health Tech, EAD (IA), Cursos e Capacitações e Tecnologia em Saúde / Desenvolvimento de Aplicativos e Tecnologias em Saúde "

```html
<!DOCTYPE html>
<html lang="pt-BR">
<head>
<meta charset="UTF-8">
<title>N7S — Papel timbrado</title>
<link rel="stylesheet" href="https://fonts.googleapis.com/css2?family=Montserrat:wght@400;500;600&display=swap">
<style>
  :root {
    --backdrop: #eceff2;
    --paper: #ffffff;
    --ink: #3c4654;
    --ink-soft: #6a7483;
    --brand-blue: #1e9ad6;
    --shadow: rgba(30, 50, 70, 0.14);
  }
  * { box-sizing: border-box; margin: 0; padding: 0; }
  html, body {
    width: 1200px; height: 1200px; overflow: hidden;
    background: var(--backdrop);
    font-family: "Montserrat", sans-serif;
  }
  .stage {
    width: 1200px; height: 1200px;
    display: flex; align-items: center; justify-content: center;
  }
  .letterhead {
    position: relative;
    width: 720px; height: 1018px;
    background: var(--paper);
    box-shadow: 0 10px 40px var(--shadow);
  }
  .brand {
    position: absolute; top: 70px; left: 0; right: 0;
    display: flex; align-items: center; justify-content: center; gap: 16px;
  }
  .brand__name {
    font-size: 40px; font-weight: 600; color: var(--brand-blue);
    letter-spacing: 1px;
  }
  .brand__divider {
    width: 1px; height: 34px; background: var(--ink-soft);
  }
  .brand__tagline {
    font-size: 9px; font-weight: 500; color: var(--ink-soft);
    letter-spacing: 1.6px; text-transform: uppercase; line-height: 1.5;
  }
  .contacts {
    position: absolute; left: 40px; right: 40px; bottom: 44px;
    display: flex; gap: 40px;
    font-size: 10.5px; color: var(--ink); line-height: 1.9;
  }
  .contacts__group { display: flex; flex-direction: column; }
  .contacts__item { display: flex; align-items: center; gap: 8px; }
  .contacts__item strong { font-weight: 600; }
  .contacts__icon { width: 12px; height: 12px; flex: none; }
  .footer-band {
    position: absolute; right: 0; bottom: 0;
    width: 58%; height: 16px; background: var(--brand-blue);
  }
</style>
</head>
<body>
<main class="stage">
  <article class="letterhead">
    <header class="brand">
      <span class="brand__name">N7S</span>
      <span class="brand__divider"></span>
      <span class="brand__tagline">Novas Soluções<br>em Saúde</span>
    </header>

    <footer class="contacts">
      <div class="contacts__group">
        <span class="contacts__item">
          <svg class="contacts__icon" viewBox="0 0 12 12"><circle cx="6" cy="6" r="6" fill="#1e9ad6"/><path d="M4 3.2l1 1.6-.6.7c.4.9 1.1 1.6 2 2l.7-.6 1.6 1-.5 1.1C5.5 8.9 3.1 6.5 3 3.7z" fill="#fff"/></svg>
          <strong>(83) 90000-4150</strong>
        </span>
        <span class="contacts__item">
          <svg class="contacts__icon" viewBox="0 0 12 12"><circle cx="6" cy="6" r="6" fill="#1e9ad6"/><circle cx="6" cy="6" r="3.2" fill="none" stroke="#fff" stroke-width="1"/><path d="M2.8 6h6.4M6 2.8v6.4" stroke="#fff" stroke-width=".8"/></svg>
          <span>www.n7saude.com.br</span>
        </span>
      </div>
      <div class="contacts__group">
        <span class="contacts__item">
          <svg class="contacts__icon" viewBox="0 0 12 12"><circle cx="6" cy="6" r="6" fill="#1e9ad6"/><path d="M6 2.5a2.3 2.3 0 0 1 2.3 2.3C8.3 6.6 6 9.5 6 9.5S3.7 6.6 3.7 4.8A2.3 2.3 0 0 1 6 2.5z" fill="#fff"/><circle cx="6" cy="4.8" r=".8" fill="#1e9ad6"/></svg>
          <span>Rua das Acácias, 210 - Sala 04 - Caixa Postal 118</span>
        </span>
        <span class="contacts__item">
          <span class="contacts__icon"></span>
          <span>Bairro Jardim - Vila Serena - PB - CEP 58.000-100</span>
        </span>
      </div>
    </footer>
    <div class="footer-band"></div>
  </article>
</main>
</body>
</html>
```